Business card/ stationary design for a pressure washing company
Commercial and Residential
Business card/ stationary design for a pressure washing company - Cleaning
Creative Brief
Simple
Marcus Delgado
N/A
Brookrinse@mailbox-demo.com
www.brookrinse-demo.com
Open to the idea of single or double sided business cards
brookrinse brookrinse
I have gone through the submissions that I have received so far and indicated a couple from each designer that I like. If you could please take that and apply it into a full stationary demo as well as a vehicle magnet, I would love to see how the design ideas transfer into the various applications. Thanks, Marcus
Also, a vehicle magnet would be very useful. Thanks!

```html
<!DOCTYPE html>
<html lang="en">
<head>
<meta charset="utf-8">
<title>Brookrinse Business Cards</title>
<link href="https://fonts.googleapis.com/css2?family=Montserrat:wght@400;600;800&display=swap" rel="stylesheet">
<style>
  :root{
    --bg:#2b2b2d;
    --card:#ffffff;
    --blue:#1f63d6;
    --navy:#0d2f8a;
    --ink:#2a2a2a;
    --muted:#6a6f78;
  }
  *{margin:0;padding:0;box-sizing:border-box}
  html,body{width:1200px;height:698px;overflow:hidden}
  body{background:var(--bg);font-family:'Montserrat',sans-serif;position:relative}
  .card{position:absolute;width:520px;height:297px;background:var(--card);border-radius:14px;overflow:hidden;box-shadow:0 10px 30px rgba(0,0,0,.35)}
  .card-front{left:50px;top:200px}
  .card-back{left:630px;top:200px}

  .brand{display:flex;align-items:center;gap:12px}
  .brand-dot{width:22px;height:22px;border-radius:50%;background:var(--blue)}
  .brand-name{font-weight:800;font-size:44px;color:var(--blue);letter-spacing:1px}

  .card-front .brand{position:absolute;left:0;right:0;top:95px;justify-content:center}
  .front-url{position:absolute;left:0;right:0;top:190px;text-align:center;font-size:13px;letter-spacing:2.5px;color:var(--ink)}

  .back-shape{position:absolute;inset:0}
  .card-back .brand{position:absolute;left:34px;top:94px}
  .card-back .brand-name{font-size:34px}
  .card-back .brand-dot{width:18px;height:18px}
  .holder{position:absolute;left:34px;top:192px}
  .holder-name{font-size:13px;font-weight:600;color:var(--blue);letter-spacing:1px;text-transform:uppercase}
  .holder-role{font-size:9px;color:var(--muted);letter-spacing:1.5px;text-transform:uppercase;margin-top:2px}
  .address{position:absolute;left:34px;top:254px;font-size:9px;color:#fff;line-height:1.45;letter-spacing:.5px}

  .contacts{position:absolute;right:20px;top:104px;list-style:none;color:#fff;font-size:9px;letter-spacing:.4px}
  .contacts li{display:flex;align-items:center;justify-content:flex-end;gap:7px;height:17px}
  .contacts svg{width:10px;height:10px;fill:#fff}
</style>
</head>
<body>

<section class="card card-front" aria-label="Card front">
  <div class="brand">
    <span class="brand-dot"></span>
    <span class="brand-name">Brookrinse</span>
  </div>
  <p class="front-url">www.brookrinse-demo.com</p>
</section>

<section class="card card-back" aria-label="Card back">
  <svg class="back-shape" viewBox="0 0 520 297" preserveAspectRatio="none">
    <path d="M370 0 H520 V297 H0 V248 C190 248 340 185 370 0Z" fill="var(--blue)"/>
    <path d="M352 0 C330 170 200 236 0 240" fill="none" stroke="var(--navy)" stroke-width="5"/>
  </svg>

  <div class="brand">
    <span class="brand-dot"></span>
    <span class="brand-name">Brookrinse</span>
  </div>

  <div class="holder">
    <p class="holder-name">Marcus Delgado</p>
    <p class="holder-role">President</p>
  </div>

  <p class="address">42 Maple Creek Blvd<br>Suite 100, Riverton ST</p>

  <ul class="contacts">
    <li>555 010 2233 <svg viewBox="0 0 10 10"><path d="M2 0.5 L3.8 2.6 L3 3.8 C3.8 5.4 4.6 6.2 6.2 7 L7.4 6.2 L9.5 8 L8.4 9.5 C4.5 9.3 .7 5.5 .5 1.6Z"/></svg></li>
    <li>555 010 2244 <svg viewBox="0 0 10 10"><path d="M2.5 0 H7.5 V10 H2.5Z M3.3 1 V8 H6.7 V1Z"/></svg></li>
    <li>555 010 2255 <svg viewBox="0 0 10 10"><path d="M1 1.5 H9 V6.5 H1Z M3 7 H7 V8.5 H3Z"/></svg></li>
    <li>Brookrinse@mailbox-demo.com <svg viewBox="0 0 10 10"><path d="M0.5 2 H9.5 V8.5 H0.5Z M1 2.4 L5 5.6 L9 2.4 V3 L5 6.3 L1 3Z"/></svg></li>
    <li>www.brookrinse-demo.com <svg viewBox="0 0 10 10"><circle cx="5" cy="5" r="4.5"/></svg></li>
  </ul>
</section>

</body>
</html>
```